100-Page Product Catalog Design for Garage Door Company (Print + Digital)

I need a professional graphic designer with extensive Adobe InDesign experience to create a high-end customer sales catalog for my garage door company, Hometown Overhead Portal Service LLC.
Important: I am an authorized GateVerve dealer and HoistPrime dealer. I have permission to use the manufacturer brochures, product images, and marketing materials in this catalog.
The finished catalog should look similar in quality to a Vantro, Morris Kettleby, or GateVerve manufacturer catalog while being fully branded for my company.
Scope of Work
Design a professionally laid out catalog approximately 80–120 pages including:
* Custom front and back cover
* Table of contents
* Company introduction
* Why choose Hometown Overhead Portal Service LLC
* GateVerve garage door collections
* Large product photos
* Construction diagrams
* Colors
* Window options
* Decorative hardware
* HoistPrime opener section
* Comparison charts
* Installed pricing tables
* Warranty
* Financing
* Contact information
* QR codes
* Print-ready layout
Materials I Will Provide
* GateVerve dealer brochures (PDF)
* HoistPrime product guides (PDF)
* Company logo
* Installed pricing
* Company information
* Contact information
* Branding requirements
Deliverables Required
* Adobe InDesign (.INDD) source files
* Linked images folder
* Print-ready PDF (300 DPI with bleed)
* Web-optimized PDF
* Editable text
* All fonts used or a font list
Style
The catalog should have a clean, modern, premium appearance suitable for homeowners purchasing garage doors in the $2,000–$8,000 range.
The design should feel comparable to a national manufacturer catalog while promoting Hometown Overhead Portal Service LLC as a local premium dealer.
Experience Required
Please send examples of:
* Product catalogs
* Manufacturer brochures
* Home improvement catalogs
* Construction or building products
* Print publications created in Adobe InDesign
Additional Information:
I have uploaded all of the GateVerve and HoistPrime dealer brochures. I am an authorized dealer and have permission to use these marketing materials in my catalog.
I do not want the brochures simply combined into one PDF. I want a completely redesigned, professional catalog branded as Hometown Overhead Portal Service LLC using the brochure content as source material.
Please create a premium customer sales catalog suitable for professional printing and online viewing. The design should look comparable to a major manufacturer’s catalog and be fully editable in Adobe InDesign.
* Editable InDesign file (.INDD)
* Web PDF
* Master pages and paragraph styles for easy future updates
* Linked image files included
* Space for pricing pages that can be updated later
Budget
Please quote a fixed price and estimated completion time.

```html
<!DOCTYPE html>
<html lang="en">
<head>
<meta charset="utf-8">
<title>Garage Door Collection 2026 – Cover and Contents</title>
<link href="https://fonts.googleapis.com/css2?family=Playfair+Display:wght@400;700;800&family=Manrope:wght@300;400&display=swap" rel="stylesheet">
<style>
  :root {
    --ink: #000000;
    --paper: #ffffff;
    --gold: #d98a2b;
    --text-dark: #2a2a2a;
    --rule: #bdbdbd;
    --edge-blue: #1a1ad0;
    --photo-top: #4b4658;
    --photo-mid: #5a4a42;
    --thumb-top: #8a6552;
    --thumb-bottom: #3e3d44;
  }
  * { margin: 0; padding: 0; box-sizing: border-box; }
  html, body { width: 1200px; height: 777px; overflow: hidden; background: var(--paper); }
  .spread { position: relative; width: 1200px; height: 777px; overflow: hidden; }

  /* Cover */
  .cover { position: absolute; left: 0; top: 0; width: 600px; height: 777px; background: var(--ink); overflow: hidden; }
  .cover-photo {
    position: absolute; inset: 0;
    background: linear-gradient(180deg, var(--photo-top) 0%, var(--photo-mid) 45%, #1c1917 68%, var(--ink) 85%);
  }
  .company-name {
    position: absolute; left: 69px; top: 40px;
    font-family: "Playfair Display", serif; font-weight: 400;
    font-size: 17px; line-height: 16.5px; color: var(--paper); letter-spacing: 0.3px;
  }
  .title-rule { position: absolute; left: 70px; top: 413px; width: 73px; height: 3px; background: var(--gold); }
  .title {
    position: absolute; left: 68px; top: 430px;
    font-family: "Playfair Display", serif; font-weight: 800; color: var(--paper);
    font-variant-numeric: lining-nums;
  }
  .title-kicker { display: block; font-size: 29px; line-height: 36px; letter-spacing: -0.5px; }
  .title-main { display: block; font-size: 47px; line-height: 46px; letter-spacing: -1px; margin-top: 8px; }
  .title-year { display: block; font-size: 47px; line-height: 48px; color: var(--gold); font-variant-numeric: lining-nums; }
  .tagline {
    position: absolute; left: 67px; top: 659px;
    font-family: "Manrope", sans-serif; font-weight: 300;
    font-size: 23px; line-height: 28px; color: var(--paper);
  }

  /* Contents page */
  .contents { position: absolute; left: 600px; top: 0; width: 405px; height: 777px; background: var(--paper); }
  .contents-heading {
    position: absolute; left: 41px; top: 146px;
    font-family: "Playfair Display", serif; font-weight: 700; font-size: 24px; color: var(--text-dark);
  }
  .toc { position: absolute; left: 42px; top: 229px; width: 250px; list-style: none;
    font-family: "Manrope", sans-serif; font-weight: 400; font-size: 11.5px; color: var(--text-dark); }
  .toc-item { position: relative; height: 25.7px; display: flex; align-items: center; }
  .toc-num { width: 26px; }
  .toc-label { flex: 1; }
  .toc-page { position: absolute; right: 0; width: 39px; text-align: center; height: 100%;
    display: flex; align-items: center; justify-content: center; }
  .toc-item:not(:last-child) .toc-page { border-bottom: 1px solid var(--rule); }

  /* Gallery strip */
  .gallery { position: absolute; left: 1005px; top: 0; width: 195px; height: 777px; background: var(--ink); border-left: 1px solid var(--edge-blue); }
  .thumb {
    position: absolute; left: 936px; width: 215px; height: 143px;
    background: linear-gradient(180deg, var(--thumb-top) 0%, var(--thumb-bottom) 100%);
  }
  .thumb-1 { top: 130px; }
  .thumb-2 { top: 317px; }
  .thumb-3 { top: 504px; }
</style>
</head>
<body>
<div class="spread">
  <section class="cover">
    <div class="cover-photo" role="img" aria-label="Photo: white farmhouse with dark garage doors and lit porch at dusk"></div>
    <p class="company-name">HOMETOWN<br>OVERHEAD PORTAL SERVICE<br>LLC</p>
    <div class="title-rule"></div>
    <h1 class="title">
      <span class="title-kicker">THE COMPLETE</span>
      <span class="title-main">GARAGE DOOR<br>COLLECTION</span>
      <span class="title-year">2026</span>
    </h1>
    <p class="tagline">Beautiful Homes<br>Begin at the Garage.</p>
  </section>

  <section class="contents">
    <h2 class="contents-heading">CONTENTS</h2>
    <ol class="toc">
      <li class="toc-item"><span class="toc-num">01</span><span class="toc-label">Welcome</span><span class="toc-page">01</span></li>
      <li class="toc-item"><span class="toc-num">02</span><span class="toc-label">Why Homeowners Choose Us</span><span class="toc-page">02</span></li>
      <li class="toc-item"><span class="toc-num">04</span><span class="toc-label">Garage Door Collections</span><span class="toc-page">03</span></li>
      <li class="toc-item"><span class="toc-num">03</span><span class="toc-label">Traditional Collection</span><span class="toc-page">12</span></li>
      <li class="toc-item"><span class="toc-num">05</span><span class="toc-label">Carriage House Collection</span><span class="toc-page">22</span></li>
      <li class="toc-item"><span class="toc-num">06</span><span class="toc-label">Contemporary Collection</span><span class="toc-page">46</span></li>
      <li class="toc-item"><span class="toc-num">07</span><span class="toc-label">Flush Collection</span><span class="toc-page">54</span></li>
      <li class="toc-item"><span class="toc-num">08.</span><span class="toc-label">Construction &amp; Insulation</span><span class="toc-page">55</span></li>
      <li class="toc-item"><span class="toc-num">09.</span><span class="toc-label">Color Options</span><span class="toc-page">66</span></li>
      <li class="toc-item"><span class="toc-num">10.</span><span class="toc-label">&nbsp;Decorative Windows</span><span class="toc-page">74</span></li>
      <li class="toc-item"><span class="toc-num">11.</span><span class="toc-label">Decorative Hardware</span><span class="toc-page">82</span></li>
      <li class="toc-item"><span class="toc-num">02.</span><span class="toc-label">HoistPrime Smart Openers</span><span class="toc-page">90</span></li>
      <li class="toc-item"><span class="toc-num">03,</span><span class="toc-label">Product Comparison Guide</span><span class="toc-page">96</span></li>
      <li class="toc-item"><span class="toc-num">14</span><span class="toc-label">Warranty &amp; Financing</span><span class="toc-page">100</span></li>
      <li class="toc-item"><span class="toc-num">15.</span><span class="toc-label">Contact Us</span><span class="toc-page">120</span></li>
    </ol>
  </section>

  <aside class="gallery"></aside>
  <div class="thumb thumb-1" role="img" aria-label="Photo: farmhouse with three-car garage at sunset"></div>
  <div class="thumb thumb-2" role="img" aria-label="Photo: farmhouse with three-car garage at sunset"></div>
  <div class="thumb thumb-3" role="img" aria-label="Photo: farmhouse with three-car garage at sunset"></div>
</div>
</body>
</html>
```